Velko Prime seamless gutters and drains

I need a cool, modern, sleek design for m-370 crew cab trucks and 16’ box trucks. I’m not wanting full wraps but I want like a half wrap in the center of the vehicles. Blue background with white logo. With website and phone number only.

velkoprime.example
317.804.2196

Target Market(s)

Homeowners and contractors

Industry/Entity Type

Seamless gutters and drainage

Font styles to use
Sans Serif

Colors
0054AA
0677BA
7BADD7
CADEEF
E8F1F8

Requirements
Must have
• Blue background with white logo and white lettering
Nice to have
• Blue background with curvatures and white logo and lettering in the middle of the box truck and m-370’s

```html
<!DOCTYPE html>
<html lang="en">
<head>
<meta charset="utf-8">
<title>Velko Prime – Vehicle Graphics</title>
<link rel="stylesheet" href="https://fonts.googleapis.com/css2?family=Oswald:wght@500;600;700&display=swap">
<style>
  :root {
    --blue-deep: #0047AB;
    --blue-mid: #0677BA;
    --blue-sky: #14ACE0;
    --blue-soft: #7BADD7;
    --blue-pale: #CADEEF;
    --blue-mist: #E8F1F8;
    --box-grey: #ECEFF2;
    --white: #FFFFFF;
    --font: "Oswald", "Arial Narrow", sans-serif;
  }
  * { margin: 0; padding: 0; box-sizing: border-box; }
  html, body { width: 847px; height: 1200px; overflow: hidden; background: var(--white); }
  body { position: relative; font-family: var(--font); }

  .graphic { position: absolute; }
  .graphic svg.wave { position: absolute; inset: 0; width: 100%; height: 100%; }

  .brand {
    position: absolute;
    display: flex; align-items: center; gap: 8px;
    font-weight: 600; color: var(--blue-mid); white-space: nowrap; line-height: 1;
  }
  .brand .dot { border-radius: 50%; background: var(--blue-sky); flex: none; }
  .brand--white { color: var(--white); }

  .contact {
    position: absolute; left: 0; right: 0;
    text-align: center; color: var(--white); font-weight: 600; line-height: 1;
  }
  .contact .web { letter-spacing: -0.5px; }
  .contact .phone { font-weight: 700; letter-spacing: -0.5px; }

  /* Pickup side graphic */
  .pickup { left: 40px; top: 70px; width: 770px; height: 200px; }
  .pickup .tagline {
    position: absolute; left: 48px; top: 80px;
    font-size: 17px; font-weight: 500; color: var(--blue-deep); letter-spacing: -0.3px;
    white-space: nowrap; line-height: 1;
  }
  .pickup .door-band { position: absolute; left: 268px; top: 62px; width: 322px; height: 132px; }
  .pickup .brand { left: 20px; top: 78px; font-size: 16px; }
  .pickup .brand .dot { width: 10px; height: 10px; background: var(--blue-pale); }
  .pickup .contact { left: 160px; top: 54px; }
  .pickup .contact .web { font-size: 18px; }
  .pickup .contact .phone { font-size: 22px; margin-top: 3px; }

  /* Central banner */
  .banner { left: 107px; top: 392px; width: 633px; height: 281px; }
  .banner .brand { left: 0; right: 0; top: 36px; justify-content: center; font-size: 40px; }
  .banner .brand .dot { width: 20px; height: 20px; }
  .banner .contact { top: 160px; }
  .banner .contact .web { font-size: 50px; }
  .banner .contact .phone { font-size: 56px; margin-top: 4px; }

  /* Box truck side graphic */
  .box { left: 48px; top: 785px; width: 484px; height: 225px; }
  .box .brand { left: 0; right: 0; top: 28px; justify-content: center; font-size: 30px; }
  .box .brand .dot { width: 15px; height: 15px; }
  .box .contact { top: 130px; }
  .box .contact .web { font-size: 38px; }
  .box .contact .phone { font-size: 42px; margin-top: 3px; }
</style>
</head>
<body>

  <section class="graphic pickup" aria-label="Pickup side graphic">
    <p class="tagline">Seamless Gutters &amp; Drainage</p>
    <div class="door-band">
      <svg class="wave" viewBox="0 0 322 132" preserveAspectRatio="none" aria-hidden="true">
        <path d="M0 0 C40 30 100 40 170 28 S290 12 322 18 L322 132 L0 132 Z" fill="var(--blue-sky)"/>
        <path d="M0 8 C40 38 100 48 170 36 S290 20 322 26 L322 132 L0 132 Z" fill="var(--blue-deep)"/>
      </svg>
      <div class="brand brand--white"><span class="dot"></span>Velko Prime</div>
      <div class="contact">
        <div class="web">velkoprime.example</div>
        <div class="phone">317.804.2196</div>
      </div>
    </div>
  </section>

  <section class="graphic banner" aria-label="Side banner artwork">
    <svg class="wave" viewBox="0 0 633 281" preserveAspectRatio="none" aria-hidden="true">
      <path d="M0 150 C90 100 220 95 340 108 S560 110 633 60 L633 281 L0 281 Z" fill="var(--blue-sky)"/>
      <path d="M0 170 C90 122 220 117 340 128 S560 132 633 82 L633 281 L0 281 Z" fill="var(--blue-deep)"/>
    </svg>
    <div class="brand"><span class="dot"></span>Velko Prime</div>
    <div class="contact">
      <div class="web">velkoprime.example</div>
      <div class="phone">317.804.2196</div>
    </div>
  </section>

  <section class="graphic box" aria-label="Box truck side graphic">
    <svg class="wave" viewBox="0 0 484 225" preserveAspectRatio="none" aria-hidden="true">
      <rect width="484" height="225" fill="var(--box-grey)"/>
      <path d="M0 120 C70 82 170 78 260 88 S430 88 484 50 L484 225 L0 225 Z" fill="var(--blue-sky)"/>
      <path d="M0 134 C70 96 170 92 260 101 S430 102 484 64 L484 225 L0 225 Z" fill="var(--blue-deep)"/>
    </svg>
    <div class="brand"><span class="dot"></span>Velko Prime</div>
    <div class="contact">
      <div class="web">velkoprime.example</div>
      <div class="phone">317.804.2196</div>
    </div>
  </section>

</body>
</html>
```